Online nutrition company needs 3 executions of a web ad for FB marketing

We need an ad that will be used on Facebook to create curiosity about our 30 Day Vital Renewal Plan program and encourage people to think about doing the program in November or early December before the Christmas holiday period.

Dimensions: 560 pixels wide by 292 pixels high

3 Versions required with:
A common headline and 'footer'
A Sub-line and a few key message points
An impactful image to support the sub-line

Headline: It's NOW O'clock
Footer: Vorantel Nutrition - Answers for All. Start NOW and feel fantastic for the holidays! Contact the person who shared this to get started today.

All 3 versions should have a similar architecture and look like they are from the same campaign. Yet the 3 message images can have a different look and feel which is unique to the specific sub-line targeting.

Version 1 Sub-Line: Be Little Black Dress Ready
Points: Look hot and healthy for the holidays
Feel revitalized, energized and alive!
Image/Visual direction: party/cocktail dress, dark, evening party, sophisticated flirty

Version 2 Sub-Line: Energize your Holidays
Points: Give yourself the energy to handle any stress that comes your way!
Image/Visual direction: bright/light, frustrated or exasperated women or male & female couple, stressed or tired from holiday/christmas related activities.

Version 3 Sub-line: Give Yourself a Gift
Points: You deserve to look and feel your best
Taking care of yourself allows you to take care of everyone else
Image/Visual direction: Happy healthy person/people, fit, a 'bow around their waist", energized

We'd like to see designs that are energetic, bold, bright yet sophisticated that will breakthrough the clutter of a busy Facebook newsfeed.

We are independent distributors of Vorantel products. Check out www.vorantel-example.com to see more about the products and background. Note that we're not necessarily trying to replicate the look and feel of the Vorantel website. We want to be more breakthrough and urgent.

Target Market(s)

Primarily women aged 35-60 who are looking to take care of their health, specifically who are looking to loose a little (not a lot) of weight.
Secondary target is men 40-60 looking lose a little weight.

In both cases they have above average incomes

Industry/Entity Type

Architecture

Requirements
Should not have
• No need to add any reference to "buy now" or "order here".
No 'call to action' buttons required.

```html
<!DOCTYPE html>
<html lang="en">
<head>
<meta charset="utf-8">
<title>It's Now O'Clock – Vorantel Holiday Ad</title>
<link rel="stylesheet" href="https://fonts.googleapis.com/css2?family=Oswald:wght@600;700&family=Arimo:wght@400;700&display=swap">
<style>
  :root {
    --lime: #8cc63f;
    --ink: #2b2b2b;
    --grey-text: #3a3a3a;
    --board: #262626;
    --board-text: #f4f4f4;
    --footer-bg: #f1f1f1;
    --paper: #ffffff;
    --photo-dark: #3a2a22;
    --photo-skin: #b98462;
    --photo-light: #eee9e4;
  }
  * { margin: 0; padding: 0; box-sizing: border-box; }
  html, body { width: 1200px; height: 626px; overflow: hidden; background: var(--paper); }
  .ad {
    position: relative;
    width: 1200px;
    height: 626px;
    background: var(--paper);
    font-family: "Arimo", Arial, sans-serif;
    color: var(--grey-text);
    overflow: hidden;
  }
  .headline {
    position: absolute;
    left: 43px; top: 30px;
    font-family: "Oswald", "Arial Narrow", sans-serif;
    font-weight: 700;
    font-size: 76px;
    line-height: 1;
    letter-spacing: 1px;
    color: var(--lime);
    text-transform: uppercase;
  }
  .subline {
    position: absolute;
    left: 43px; top: 145px;
    font-weight: 700;
    font-size: 31px;
    color: var(--ink);
    text-transform: uppercase;
    letter-spacing: 0.2px;
  }
  .point {
    position: absolute;
    left: 43px;
    font-size: 33px;
    line-height: 1.2;
    color: var(--grey-text);
    text-transform: uppercase;
  }
  .point--look { top: 228px; }
  .point--feel { top: 368px; }
  .brand {
    position: absolute;
    left: 832px; top: 50px;
    display: flex; align-items: center; gap: 12px;
    z-index: 3;
  }
  .brand__mark { width: 22px; height: 22px; border-radius: 50%; background: var(--lime); }
  .brand__name {
    font-family: "Arimo", Arial, sans-serif;
    font-weight: 700;
    font-size: 38px;
    color: var(--ink);
    text-transform: uppercase;
    letter-spacing: 1px;
  }
  .model-photo {
    position: absolute;
    left: 900px; top: 0;
    width: 300px; height: 523px;
    background: linear-gradient(180deg, var(--photo-light) 0%, var(--photo-dark) 22%, var(--photo-skin) 45%, var(--photo-dark) 62%, var(--photo-skin) 80%, var(--photo-light) 100%);
    z-index: 1;
  }
  .party-board {
    position: absolute;
    left: 553px; top: 214px;
    width: 386px; height: 283px;
    background: var(--board);
    padding: 28px 30px 0 41px;
    z-index: 2;
  }
  .party-board p {
    font-size: 31px;
    line-height: 1.5;
    color: var(--board-text);
    text-transform: uppercase;
  }
  .rule {
    position: absolute;
    left: 0; top: 523px;
    width: 1200px; height: 13px;
    background: var(--lime);
  }
  .footer {
    position: absolute;
    left: 0; top: 536px;
    width: 1200px; height: 90px;
    background: var(--footer-bg);
    display: flex; flex-direction: column; justify-content: center; align-items: center;
    font-size: 24px;
    line-height: 1.3;
    color: var(--grey-text);
    text-align: center;
  }
</style>
</head>
<body>
  <div class="ad">
    <h1 class="headline">It's Now O'Clock</h1>
    <h2 class="subline">It's Little Black Dress Season</h2>
    <p class="point point--look">Look hot and healthy<br>for the holidays</p>
    <p class="point point--feel">Feel revitalized,<br>energized and alive!</p>

    <div class="brand">
      <span class="brand__mark"></span>
      <span class="brand__name">Vorantel</span>
    </div>

    <div class="model-photo" role="img" aria-label="Photo of a slim woman in a black strapless top and bead necklaces holding a sign"></div>

    <div class="party-board">
      <p>Imaging<br>fitting<br>easily into<br>your party<br>dress</p>
    </div>

    <div class="rule"></div>

    <footer class="footer">
      <p>Start a Vorantel 30 Day Vital Renewal Plan NOW and be fantastic for the holidays!</p>
      <p>Contact the person who shared this to get started today.</p>
    </footer>
  </div>
</body>
</html>
```